A bar in Newtown, NSW needs a website

We need a website design for a small speakeasy-style bar in Newtown, NSW Australia. The website needs to be simple to navigate, minimalistic, and feature light colours.

The functionality has to be fairly simple:

Main page (navigates to things below)
Food menu
Beverage menu
Bookings

Social media links and misc info at the bottom of every page.

The menus pages need to have space for text inserted as a jpeg file.

Name and logo are attached.

Coded - Design and coding required

4 page

```html
<!DOCTYPE html>
<html lang="en">
<head>
<meta charset="utf-8">
<title>The Copper Lantern — Bar, Newtown</title>
<link rel="stylesheet" href="https://fonts.googleapis.com/css2?family=Bebas+Neue&family=Montserrat:wght@500;600;700&family=Playfair+Display:ital,wght@1,700&family=Raleway:wght@400;500&family=Roboto+Slab:wght@300;400;700&display=swap">
<style>
  :root {
    --ink: #151515;
    --band: #1c1c1c;
    --white: #ffffff;
    --muted: #555555;
    --line: #3a3a3a;
    --tab-line: #c9cdd6;
    --tab-text: #5a6275;
    --amber: #e39a12;
    --footer-text: #666666;
  }
  * { box-sizing: border-box; margin: 0; padding: 0; }
  html, body { width: 1200px; height: 3035px; overflow: hidden; }
  body { position: relative; background: var(--white); color: var(--ink); font-family: "Raleway", sans-serif; }

  /* Navigation */
  .site-nav { position: absolute; top: 0; left: 0; width: 1200px; height: 101px; background: var(--white); }
  .nav-link { position: absolute; top: 38px; height: 33px; line-height: 33px; font-family: "Montserrat", sans-serif; font-weight: 600; font-size: 12px; letter-spacing: .5px; color: var(--ink); text-decoration: none; text-transform: uppercase; }
  .nav-link.is-active { background: var(--ink); color: var(--white); padding: 0 16px; }
  .nav-menu { left: 285px; }
  .nav-food { left: 395px; }
  .nav-bev { left: 769px; }
  .nav-book { left: 931px; }
  .brand { position: absolute; left: 540px; top: 22px; width: 160px; text-align: center; font-family: "Roboto Slab", serif; font-weight: 400; font-size: 22px; line-height: 26px; color: var(--ink); }

  /* Hero */
  .hero { position: absolute; top: 101px; left: 0; width: 1200px; height: 583px; }
  .hero-photo { position: absolute; inset: 0; background: radial-gradient(ellipse at 55% 70%, #b88424 0%, #6b4a16 30%, #2b1f10 60%, #0e0b07 100%); }
  .hero-title { position: absolute; top: 180px; width: 100%; text-align: center; font-family: "Roboto Slab", serif; font-weight: 400; font-size: 52px; color: var(--white); }
  .hero-text { position: absolute; top: 252px; left: 350px; width: 500px; text-align: center; font-size: 16px; line-height: 25px; color: #f1e6d2; }
  .hero-cta { position: absolute; top: 344px; left: 542px; width: 146px; height: 45px; border: 2px solid var(--white); color: var(--white); }
  .dots { position: absolute; top: 557px; left: 586px; display: flex; gap: 5px; }
  .dots span { width: 7px; height: 7px; border-radius: 50%; border: 1px solid var(--white); }
  .dots span.on { background: var(--white); }

  /* Buttons */
  .btn { display: flex; align-items: center; justify-content: center; font-family: "Bebas Neue", sans-serif; font-size: 19px; letter-spacing: .5px; text-decoration: none; }
  .btn-outline { border: 2px solid var(--line); color: var(--ink); background: var(--white); }

  /* Menu sections */
  .menu-section { position: absolute; left: 0; width: 1200px; height: 830px; }
  .food-menu { top: 684px; }
  .beverage-menu { top: 1670px; }
  .section-title { position: absolute; top: 64px; width: 100%; text-align: center; font-family: "Roboto Slab", serif; font-weight: 400; font-size: 46px; }
  .section-intro { position: absolute; top: 140px; left: 305px; width: 590px; text-align: center; font-size: 14.5px; line-height: 24px; color: var(--muted); }
  .tab { position: absolute; top: 200px; width: 114px; height: 33px; display: flex; align-items: center; justify-content: center; font-family: "Montserrat", sans-serif; font-size: 11px; font-weight: 500; color: var(--tab-text); border: 1px solid var(--tab-line); text-transform: uppercase; }
  .tab.is-active { background: var(--ink); border-color: var(--ink); color: var(--white); }
  .tab-1 { left: 397px; } .tab-2 { left: 542px; } .tab-3 { left: 688px; }

  .dish { position: absolute; background: var(--white); box-shadow: 0 4px 18px rgba(0,0,0,.12); padding: 18px; }
  .dish-small { top: 332px; width: 146px; height: 146px; }
  .dish-large { top: 292px; left: 488px; width: 224px; height: 224px; padding: 26px; }
  .dish-photo { width: 100%; height: 100%; border-radius: 50%; }
  .col-1 { left: 81px; } .col-2 { left: 287px; } .col-4 { left: 765px; } .col-5 { left: 984px; }
  .dish-more { position: absolute; top: 524px; width: 146px; height: 45px; }

  .price { position: absolute; top: 540px; width: 100%; text-align: center; font-family: "Playfair Display", serif; font-style: italic; font-weight: 700; font-size: 46px; }
  .dish-name { position: absolute; top: 622px; width: 100%; text-align: center; font-family: "Montserrat", sans-serif; font-weight: 600; font-size: 16px; }
  .dish-desc { position: absolute; top: 646px; left: 500px; width: 200px; text-align: center; font-size: 12.5px; line-height: 20px; color: var(--muted); }
  .dish-book { position: absolute; top: 719px; left: 528px; width: 144px; height: 45px; }

  /* Promo band */
  .promo { position: absolute; top: 1514px; left: 0; width: 1200px; height: 166px; background: var(--band); }
  .promo-text { position: absolute; top: 66px; left: 162px; font-family: "Roboto Slab", serif; font-weight: 700; font-size: 21px; color: var(--white); }
  .promo-book { position: absolute; top: 59px; left: 747px; width: 144px; height: 45px; border: 2px solid var(--white); color: var(--white); }
  .promo-read { position: absolute; top: 59px; left: 903px; width: 143px; height: 45px; background: var(--white); color: var(--ink); }

  /* Bookings */
  .bookings { position: absolute; top: 2516px; left: 0; width: 1200px; height: 449px; }
  .bookings-photo { position: absolute; inset: 0; background: radial-gradient(ellipse at 30% 60%, #5a4121 0%, #2c2116 45%, #141210 100%); }
  .bookings-title { position: absolute; top: 64px; width: 100%; text-align: center; font-family: "Roboto Slab", serif; font-size: 50px; color: var(--white); }
  .field { position: absolute; width: 332px; height: 48px; border: 2px solid #e8e8e8; display: flex; align-items: center; justify-content: space-between; padding: 0 14px; font-family: "Bebas Neue", sans-serif; font-size: 21px; color: var(--white); }
  .row-1 { top: 170px; } .row-2 { top: 233px; }
  .fc-1 { left: 83px; } .fc-2 { left: 441px; } .fc-3 { left: 797px; }
  .booking-submit { position: absolute; top: 340px; left: 542px; width: 146px; height: 44px; background: var(--amber); color: var(--white); }

  /* Footer */
  .site-footer { position: absolute; top: 2965px; left: 0; width: 1200px; height: 70px; background: var(--white); }
  .copyright { position: absolute; top: 30px; left: 81px; font-size: 12px; color: var(--footer-text); }
  .social { position: absolute; top: 31px; left: 1044px; display: flex; gap: 10px; }
  .social span { width: 11px; height: 11px; border-radius: 50%; background: #333; }
</style>
</head>
<body>

<header class="site-nav">
  <a class="nav-link nav-menu is-active" href="#">Menu</a>
  <a class="nav-link nav-food" href="#food">Food Menu</a>
  <div class="brand">The Copper Lantern</div>
  <a class="nav-link nav-bev" href="#beverages">Beverage Menu</a>
  <a class="nav-link nav-book" href="#bookings">Bookings</a>
</header>

<section class="hero">
  <div class="hero-photo" role="img" aria-label="Photo of beer being poured from a bar tap into a glass"></div>
  <h1 class="hero-title">Praesent scelerisque sem sedt</h1>
  <p class="hero-text">Lorem ipsum dolor sit amet, consectetur adipisicing elit, sed do eiusmod tempor incididunt ut labore et dolore magna aliqua.</p>
  <a class="btn hero-cta" href="#">Learn More</a>
  <div class="dots"><span class="on"></span><span></span><span></span><span></span></div>
</section>

<section class="menu-section food-menu" id="food">
  <h2 class="section-title">Food Menu</h2>
  <p class="section-intro">Lorem ipsum dolor sit amet, consectetur adipisicing elit, sed do eiusmod tempor incididunt ut labore et dolore magna aliqua.</p>
  <div class="tab tab-1">Desserts</div>
  <div class="tab tab-2 is-active">Meats</div>
  <div class="tab tab-3">Salads</div>

  <div class="dish dish-small col-1"><div class="dish-photo" role="img" aria-label="Photo of meatballs on a white plate" style="background: radial-gradient(circle, #a0412a 0%, #e9e4df 75%);"></div></div>
  <div class="dish dish-small col-2"><div class="dish-photo" role="img" aria-label="Photo of a plated green garnish dish" style="background: radial-gradient(circle, #6e8f4a 0%, #eef0ea 75%);"></div></div>
  <div class="dish dish-large"><div class="dish-photo" role="img" aria-label="Photo of a bowl of fresh fruit salad" style="background: radial-gradient(circle, #e0762f 0%, #d9b94a 40%, #f4efe6 80%);"></div></div>
  <div class="dish dish-small col-4"><div class="dish-photo" role="img" aria-label="Photo of a filled baguette sandwich" style="background: radial-gradient(ellipse, #b9773d 0%, #f1ebe3 75%);"></div></div>
  <div class="dish dish-small col-5"><div class="dish-photo" role="img" aria-label="Photo of a bowl of noodle soup with chopsticks" style="background: radial-gradient(circle, #c86a34 0%, #e8d9c6 75%);"></div></div>

  <a class="btn btn-outline dish-more col-1" href="#">Learn More</a>
  <a class="btn btn-outline dish-more col-2" href="#">Learn More</a>
  <a class="btn btn-outline dish-more col-4" href="#">Learn More</a>
  <a class="btn btn-outline dish-more col-5" href="#">Learn More</a>

  <div class="price">34$</div>
  <div class="dish-name">Contantry Popilar</div>
  <p class="dish-desc">consectetur adipisicing elit, sed do eiusmod tempor incididunt ut labore et dolore magna aliqua</p>
  <a class="btn btn-outline dish-book" href="#">Book Now</a>
</section>

<section class="promo">
  <p class="promo-text">Lorem ipsum dolor sit amet, consectetur adipiscing elit</p>
  <a class="btn promo-book" href="#">Book Now</a>
  <a class="btn promo-read" href="#">Read More</a>
</section>

<section class="menu-section beverage-menu" id="beverages">
  <h2 class="section-title">Beverage Menu</h2>
  <p class="section-intro">Lorem ipsum dolor sit amet, consectetur adipisicing elit, sed do eiusmod tempor incididunt ut labore et dolore magna aliqua.</p>
  <div class="tab tab-1">Lorem</div>
  <div class="tab tab-2 is-active">Dolor Sit</div>
  <div class="tab tab-3">Ipsum</div>

  <div class="dish dish-small col-1"><div class="dish-photo" role="img" aria-label="Photo of a dark beer bottle" style="border-radius: 6px; background: linear-gradient(90deg, #fff 38%, #3a1f14 42%, #3a1f14 58%, #fff 62%);"></div></div>
  <div class="dish dish-small col-2"><div class="dish-photo" role="img" aria-label="Photo of a splashing glass of cola with ice" style="background: radial-gradient(circle, #7a3a14 0%, #c48b5a 40%, #f6f1ec 75%);"></div></div>
  <div class="dish dish-large"><div class="dish-photo" role="img" aria-label="Photo of a green beer bottle" style="border-radius: 8px; background: linear-gradient(90deg, #fff 36%, #2f8a2a 42%, #49b23a 50%, #2f8a2a 58%, #fff 64%);"></div></div>
  <div class="dish dish-small col-4"><div class="dish-photo" role="img" aria-label="Photo of a glass of ale beside its bottle" style="border-radius: 6px; background: linear-gradient(90deg, #fff 20%, #8a4a1c 30%, #5a2c12 70%, #fff 80%);"></div></div>
  <div class="dish dish-small col-5"><div class="dish-photo" role="img" aria-label="Photo of an orange juice cocktail with a straw" style="border-radius: 6px; background: linear-gradient(90deg, #fff 30%, #f0b04a 40%, #f5c870 60%, #fff 70%);"></div></div>

  <a class="btn btn-outline dish-more col-1" href="#">Learn More</a>
  <a class="btn btn-outline dish-more col-2" href="#">Learn More</a>
  <a class="btn btn-outline dish-more col-4" href="#">Learn More</a>
  <a class="btn btn-outline dish-more col-5" href="#">Learn More</a>

  <div class="price">34$</div>
  <div class="dish-name">Contantry Popilar</div>
  <p class="dish-desc">consectetur adipisicing elit, sed do eiusmod tempor incididunt ut labore et dolore magna aliqua</p>
  <a class="btn btn-outline dish-book" href="#">Book Now</a>
</section>

<section class="bookings" id="bookings">
  <div class="bookings-photo" role="img" aria-label="Photo of beer mugs on a dark wooden table"></div>
  <h2 class="bookings-title">Bookings</h2>
  <div class="field row-1 fc-1">Name</div>
  <div class="field row-1 fc-2">Email</div>
  <div class="field row-1 fc-3">Phone</div>
  <div class="field row-2 fc-1">Date <svg width="14" height="9" viewBox="0 0 14 9"><path d="M1 1l6 6 6-6" fill="none" stroke="#fff" stroke-width="2"/></svg></div>
  <div class="field row-2 fc-2">Time <svg width="14" height="9" viewBox="0 0 14 9"><path d="M1 1l6 6 6-6" fill="none" stroke="#fff" stroke-width="2"/></svg></div>
  <div class="field row-2 fc-3">No.of Members <svg width="14" height="9" viewBox="0 0 14 9"><path d="M1 1l6 6 6-6" fill="none" stroke="#fff" stroke-width="2"/></svg></div>
  <a class="btn booking-submit" href="#">Book Now</a>
</section>

<footer class="site-footer">
  <p class="copyright">© Copyright 2016 yoursite. All rights reserved</p>
  <div class="social" aria-label="Social media links">
    <span aria-label="Social link 1"></span>
    <span aria-label="Social link 2"></span>
    <span aria-label="Social link 3"></span>
    <span aria-label="Social link 4"></span>
  </div>
</footer>

</body>
</html>
```